Brindlecove Business Card

Looking for a new business Card layout for our company, brindlecove.

Logo Text

Standard Business Card , Name, email, phone, website. www.brindlecove-example.com

```html
<!DOCTYPE html>
<html lang="en">
<head>
<meta charset="utf-8">
<title>Brindlecove Business Card</title>
<link rel="stylesheet" href="https://fonts.googleapis.com/css2?family=Signika:wght@500;600&family=Quicksand:wght@400&display=swap">
<style>
  :root {
    --blue: #5bb7df;
    --blue-soft: #8ad0ee;
    --slate: #5c6079;
    --mist: #efefef;
    --border: #cfcfcf;
    --paper: #ffffff;
    --page: #ffffff;
  }
  * { box-sizing: border-box; margin: 0; padding: 0; }
  html, body { width: 1200px; height: 1192px; overflow: hidden; background: var(--page); }
  .sheet {
    position: relative; width: 1200px; height: 1192px;
    border: 2px solid #ececec;
  }
  .card {
    position: absolute; width: 530px; height: 324px; overflow: hidden;
  }
  .card--light { background: var(--paper); border: 2px solid var(--border); }
  .card--blue { background: var(--blue); }
  .pos-front-light { left: 36px; top: 243px; }
  .pos-front-blue { left: 623px; top: 243px; }
  .pos-back-blue { left: 36px; top: 616px; }
  .pos-back-light { left: 623px; top: 616px; }

  .card__texture {
    position: absolute; top: 0; right: 0; width: 290px; height: 100%;
  }
  .card--light .card__texture {
    background: linear-gradient(105deg, rgba(239,239,239,0) 0%, var(--mist) 30%, rgba(239,239,239,0.35) 60%, var(--mist) 90%);
  }
  .card--blue .card__texture {
    background: linear-gradient(105deg, rgba(138,208,238,0) 0%, var(--blue-soft) 30%, rgba(138,208,238,0.35) 60%, var(--blue-soft) 90%);
  }

  .brand {
    position: absolute; left: 53px; top: 62px; width: 250px;
    text-align: center;
  }
  .brand__dot {
    display: block; width: 44px; height: 44px; border-radius: 50%;
    margin: 0 auto 14px;
  }
  .brand__name {
    font-family: "Signika", sans-serif; font-weight: 600;
    font-size: 38px; line-height: 1; letter-spacing: 0.2px;
  }
  .card--light .brand__dot { background: var(--blue); }
  .card--light .brand__name { color: var(--blue); }
  .card--blue .brand__dot { background: var(--paper); }
  .card--blue .brand__name { color: var(--paper); }

  .holder {
    position: absolute; left: 53px; top: 190px; width: 250px; text-align: center;
    font-family: "Signika", sans-serif; font-weight: 500; font-size: 33px;
    color: var(--slate); line-height: 1;
  }

  .contacts { position: absolute; left: 36px; top: 42px; list-style: none; }
  .contacts__row {
    display: flex; align-items: center; height: 27px; margin-bottom: 14.5px;
    font-family: "Quicksand", sans-serif; font-size: 21px; line-height: 1;
  }
  .contacts__icon {
    width: 27px; height: 27px; border-radius: 50%; margin-right: 21px;
    display: flex; align-items: center; justify-content: center; flex: none;
  }
  .contacts__icon svg { width: 15px; height: 15px; }
  .card--blue .contacts__row { color: var(--paper); }
  .card--blue .contacts__icon { background: var(--paper); color: var(--blue); }
  .card--light .contacts__row { color: var(--slate); }
  .card--light .contacts__icon { background: var(--slate); color: var(--paper); }
  .icon-defs { position: absolute; width: 0; height: 0; }
</style>
</head>
<body>
<svg class="icon-defs" aria-hidden="true">
  <defs>
    <symbol id="i-pin" viewBox="0 0 16 16"><path fill="currentColor" d="M8 1a5 5 0 0 0-5 5c0 3.6 5 9 5 9s5-5.4 5-9a5 5 0 0 0-5-5zm0 7a2 2 0 1 1 0-4 2 2 0 0 1 0 4z"/></symbol>
    <symbol id="i-phone" viewBox="0 0 16 16"><path fill="currentColor" d="M4 1.5l2.2 3-1.3 1.6c.9 1.9 2.4 3.4 4.3 4.3l1.6-1.3 3 2.2-1.1 2.5C7.3 14 2 8.7 1.5 3.1z"/></symbol>
    <symbol id="i-mail" viewBox="0 0 16 16"><g fill="none" stroke="currentColor" stroke-width="1.4"><rect x="1.5" y="3.5" width="13" height="9" rx="1"/><path d="M1.8 4l6.2 5 6.2-5M1.8 12l4.5-4M14.2 12l-4.5-4"/></g></symbol>
    <symbol id="i-web" viewBox="0 0 16 16"><g fill="none" stroke="currentColor" stroke-width="1.2"><circle cx="8" cy="8" r="6.5"/><ellipse cx="8" cy="8" rx="3" ry="6.5"/><path d="M1.5 8h13M2.5 4.8h11M2.5 11.2h11"/></g></symbol>
    <symbol id="i-dot" viewBox="0 0 16 16"><circle cx="8" cy="8" r="3.2" fill="currentColor"/></symbol>
  </defs>
</svg>

<main class="sheet">
  <section class="card card--light pos-front-light">
    <div class="card__texture" role="img" aria-label="Soft flowing bubble backdrop"></div>
    <div class="brand"><span class="brand__dot"></span><div class="brand__name">BRINDLECOVE</div></div>
    <div class="holder">Your Name</div>
  </section>

  <section class="card card--blue pos-front-blue">
    <div class="card__texture" role="img" aria-label="Soft flowing bubble backdrop"></div>
    <div class="brand"><span class="brand__dot"></span><div class="brand__name">BRINDLECOVE</div></div>
    <div class="holder">Your Name</div>
  </section>

  <section class="card card--blue pos-back-blue">
    <div class="card__texture" role="img" aria-label="Soft flowing bubble backdrop"></div>
    <ul class="contacts">
      <li class="contacts__row"><span class="contacts__icon"><svg><use href="#i-pin"/></svg></span>Address</li>
      <li class="contacts__row"><span class="contacts__icon"><svg><use href="#i-phone"/></svg></span>Phone of the Company</li>
      <li class="contacts__row"><span class="contacts__icon"><svg><use href="#i-mail"/></svg></span>Company@E-mail</li>
      <li class="contacts__row"><span class="contacts__icon"><svg><use href="#i-web"/></svg></span>Website.of the.company</li>
      <li class="contacts__row"><span class="contacts__icon"><svg><use href="#i-dot"/></svg></span>Friendwall</li>
      <li class="contacts__row"><span class="contacts__icon"><svg><use href="#i-dot"/></svg></span>Chirpline</li>
    </ul>
  </section>

  <section class="card card--light pos-back-light">
    <div class="card__texture" role="img" aria-label="Soft flowing bubble backdrop"></div>
    <ul class="contacts">
      <li class="contacts__row"><span class="contacts__icon"><svg><use href="#i-pin"/></svg></span>Address</li>
      <li class="contacts__row"><span class="contacts__icon"><svg><use href="#i-phone"/></svg></span>Phone of the Company</li>
      <li class="contacts__row"><span class="contacts__icon"><svg><use href="#i-mail"/></svg></span>Company@E-mail</li>
      <li class="contacts__row"><span class="contacts__icon"><svg><use href="#i-web"/></svg></span>Website.of the.company</li>
      <li class="contacts__row"><span class="contacts__icon"><svg><use href="#i-dot"/></svg></span>Friendwall</li>
      <li class="contacts__row"><span class="contacts__icon"><svg><use href="#i-dot"/></svg></span>Chirpline</li>
    </ul>
  </section>
</main>
</body>
</html>
```